Wavelume artwork for new single release

I need Wavelume artwork creating to release a new single on there.

The specs are:

Ideal size: 3000 x 3000 pixels
Minimum size: 1400 x 1400 pixels
Aspect ratio: 1:1 (must be a perfect square)
File format: JPG or PNG
Color space: sRGB
File size: Max 4MB

The song is called "Still, Can We Wander?"
The artist is "Milo Fenwright"

We have no images of Milo, so it really is open to imagination.

Target Market(s)

Wavelume listeners

Industry/Entity Type

Music

```html
<!DOCTYPE html>
<html lang="en">
<head>
<meta charset="utf-8">
<title>Still, Can We Wander? — Milo Fenwright</title>
<link rel="stylesheet" href="https://fonts.googleapis.com/css2?family=Montserrat:wght@800&family=Raleway:wght@500&display=swap">
<style>
  :root {
    --yellow: #ffff00;
    --yellow-soft: #ffffa8;
    --orange: #ffa060;
    --shadow-orange: #ff5a00;
    --pink: #ff4cf5;
    --hot-pink: #ff3a80;
    --magenta: #ff20f0;
    --violet: #a040d0;
    --indigo: #4a4cb8;
    --bar-start: #c040f0;
    --bar-end: #5000e8;
    --white: #ffffff;
  }
  html, body {
    margin: 0;
    padding: 0;
    width: 1200px;
    height: 1195px;
    overflow: hidden;
    background: var(--white);
  }
  .cover {
    display: block;
    width: 1200px;
    height: 1195px;
  }
  .title {
    font-family: "Montserrat", sans-serif;
    font-weight: 800;
    font-size: 300px;
    letter-spacing: 0;
  }
  .title-shadow { fill: var(--shadow-orange); }
  .title-face { fill: url(#titleFill); }
  .artist {
    font-family: "Raleway", sans-serif;
    font-weight: 500;
    font-size: 96px;
    letter-spacing: 2px;
    fill: var(--white);
  }
  .frame {
    fill: none;
    stroke: var(--white);
    stroke-width: 22;
  }
</style>
</head>
<body>
<svg class="cover" viewBox="0 0 1932 1924" preserveAspectRatio="none" xmlns="http://www.w3.org/2000/svg">
  <defs>
    <linearGradient id="baseFill" x1="0" y1="0" x2="1" y2="0">
      <stop offset="0" stop-color="#e050f0"/>
      <stop offset="0.45" stop-color="var(--pink)"/>
      <stop offset="1" stop-color="var(--hot-pink)"/>
    </linearGradient>
    <linearGradient id="depthFill" x1="0.9" y1="0.1" x2="0.1" y2="1">
      <stop offset="0" stop-color="#ff3a78" stop-opacity="0"/>
      <stop offset="0.5" stop-color="var(--violet)" stop-opacity="0.75"/>
      <stop offset="1" stop-color="var(--indigo)"/>
    </linearGradient>
    <linearGradient id="rightDepth" x1="0" y1="0" x2="0" y2="1">
      <stop offset="0.35" stop-color="#9020b0" stop-opacity="0"/>
      <stop offset="1" stop-color="#8a20b8" stop-opacity="0.8"/>
    </linearGradient>
    <radialGradient id="glowYellow" cx="0.5" cy="0.5" r="0.5">
      <stop offset="0" stop-color="var(--yellow)" stop-opacity="0.95"/>
      <stop offset="1" stop-color="var(--yellow)" stop-opacity="0"/>
    </radialGradient>
    <radialGradient id="glowPeach" cx="0.5" cy="0.5" r="0.5">
      <stop offset="0" stop-color="#f0a060" stop-opacity="0.85"/>
      <stop offset="1" stop-color="#f0a060" stop-opacity="0"/>
    </radialGradient>
    <linearGradient id="sunFill" x1="0" y1="0" x2="1" y2="0">
      <stop offset="0.03" stop-color="var(--yellow)"/>
      <stop offset="0.4" stop-color="var(--orange)"/>
      <stop offset="0.7" stop-color="#ff60b8"/>
      <stop offset="1" stop-color="var(--magenta)"/>
    </linearGradient>
    <linearGradient id="barFill" x1="0" y1="0" x2="1" y2="0">
      <stop offset="0" stop-color="var(--bar-start)"/>
      <stop offset="1" stop-color="var(--bar-end)"/>
    </linearGradient>
    <linearGradient id="titleFill" x1="0" y1="0" x2="0" y2="1">
      <stop offset="0.25" stop-color="var(--yellow)"/>
      <stop offset="1" stop-color="var(--yellow-soft)"/>
    </linearGradient>
  </defs>

  <!-- background -->
  <rect class="bg-base" width="1932" height="1924" fill="url(#baseFill)"/>
  <rect class="bg-depth" width="1932" height="1924" fill="url(#depthFill)"/>
  <rect class="bg-depth-right" width="1932" height="1924" fill="url(#rightDepth)"/>

  <!-- soft colour glows -->
  <ellipse class="glow glow-top-left" cx="0" cy="250" rx="520" ry="620" fill="url(#glowYellow)"/>
  <ellipse class="glow glow-bottom" cx="1300" cy="1960" rx="420" ry="220" fill="url(#glowYellow)"/>
  <ellipse class="glow glow-bottom-right" cx="1780" cy="1760" rx="520" ry="420" fill="url(#glowPeach)"/>

  <circle class="sun" cx="950" cy="945" r="570" fill="url(#sunFill)"/>

  <polygon class="title-bar" fill="url(#barFill)" points="435,1520 1495,1405 1495,1502 435,1617"/>

  <rect class="frame" x="108" y="110" width="1714" height="1714"/>

  <!-- title -->
  <g class="title" transform="rotate(-9.5 1000 1040)" text-anchor="middle">
    <g class="title-shadow" transform="translate(14 18)">
      <text x="990" y="730">Still,</text>
      <text x="1000" y="1050">Can We</text>
      <text x="1000" y="1370">Wander?</text>
    </g>
    <g class="title-face">
      <text x="990" y="730">Still,</text>
      <text x="1000" y="1050">Can We</text>
      <text x="1000" y="1370">Wander?</text>
    </g>
  </g>

  <text class="artist" x="966" y="1758" text-anchor="middle">MILO FENWRIGHT</text>
</svg>
</body>
</html>
```